Redesign and move to Wordpress for qorvanta.com

Our website needs a redesign and at the same time we are moving it to Wordpress. Please help us with a new digital professional look and feel.

We are an Australian Software Engineering company specialising in advanced software development using in A.I., PLatform Engineering, Integration and Cloud. See the current qorvanta.com for more information about us.

```html
<!DOCTYPE html>
<html lang="en">
<head>
<meta charset="utf-8">
<title>Qorvanta — Software Engineering</title>
<link href="https://fonts.googleapis.com/css2?family=Space+Grotesk:wght@400;500;600;700&family=Inter:wght@400;500;600&display=swap" rel="stylesheet">
<style>
:root{
  --bg:#070f17;
  --panel:#0d1b27;
  --panel-2:#112331;
  --line:#1f3445;
  --text:#eef4f8;
  --muted:#8ea3b3;
  --dim:#5b7081;
  --accent:#2fa8ff;
  --accent-2:#1d6fe0;
  --teal:#1fb5c9;
}
*{box-sizing:border-box;margin:0;padding:0}
html,body{width:1200px;height:4224px;overflow:hidden;background:var(--bg)}
body{font-family:"Inter",sans-serif;color:var(--text);position:relative}
h1,h2,h3,.display{font-family:"Space Grotesk",sans-serif}
.frame{position:absolute;left:48px;top:96px;width:1104px;height:4064px;border:1px solid var(--line);border-radius:18px;overflow:hidden;
  background:
   radial-gradient(ellipse 520px 380px at 0% 14%,rgba(31,181,201,.45),transparent 70%),
   radial-gradient(ellipse 520px 380px at 100% 14%,rgba(29,111,224,.45),transparent 70%),
   radial-gradient(ellipse 560px 420px at 0% 48%,rgba(31,181,201,.4),transparent 70%),
   radial-gradient(ellipse 560px 420px at 100% 52%,rgba(29,111,224,.4),transparent 70%),
   radial-gradient(ellipse 600px 260px at 50% 72%,rgba(47,168,255,.35),transparent 70%),
   radial-gradient(ellipse 520px 300px at 100% 88%,rgba(29,111,224,.3),transparent 70%),
   var(--bg);}
.abs{position:absolute}
.center{left:0;right:0;text-align:center}
.brand{display:flex;align-items:center;gap:8px;font-family:"Space Grotesk",sans-serif;font-weight:600;font-size:20px;color:var(--text)}
.brand .mark{width:16px;height:16px;border-radius:50%;background:var(--accent)}
.nav{top:36px;left:52px;right:52px;display:flex;align-items:center;justify-content:space-between}
.nav ul{display:flex;gap:34px;list-style:none;font-size:13px;color:var(--muted)}
.btn{display:inline-block;padding:10px 20px;border-radius:20px;font-size:12px;font-weight:500;color:#fff;background:linear-gradient(90deg,var(--accent-2),var(--accent))}
.btn-ghost{display:inline-block;padding:10px 20px;border-radius:20px;font-size:12px;color:var(--text);border:1px solid var(--line);background:rgba(255,255,255,.03)}
.eyebrow{font-size:11px;letter-spacing:.12em;color:var(--accent);text-transform:uppercase;font-weight:600}
.hero-title{top:160px;font-size:44px;font-weight:700;line-height:1.1;letter-spacing:.01em}
.hero-title span{color:var(--accent)}
.hero-sub{top:262px;width:520px;left:292px;font-size:13px;color:var(--muted);line-height:1.5;text-align:center}
.ghost-word{font-family:"Space Grotesk",sans-serif;font-weight:700;font-size:190px;color:rgba(255,255,255,.04);letter-spacing:.02em;text-align:center;left:0;right:0;line-height:1}
.card{background:rgba(13,27,39,.88);border:1px solid var(--line);border-radius:14px}
.section-title{font-size:34px;font-weight:600;line-height:1.2}
.svc-grid{display:grid;grid-template-columns:1fr 1fr;gap:26px;position:absolute;left:44px;right:44px;top:176px}
.svc{background:var(--panel-2);border:1px solid var(--line);border-radius:10px;padding:24px;height:162px;position:relative}
.svc .ico{width:30px;height:30px;border-radius:8px;border:1px solid var(--line);display:flex;align-items:center;justify-content:center;margin-bottom:22px}
.svc .arrow{position:absolute;right:24px;top:24px;width:34px;height:34px;border-radius:50%;background:#17324a;display:flex;align-items:center;justify-content:center}
.svc h3{font-size:14px;letter-spacing:.04em;font-weight:600;margin-bottom:10px}
.svc p{font-size:11px;color:var(--muted);line-height:1.6}
.stats{display:flex;justify-content:center;gap:110px;font-size:11px;color:var(--muted);text-align:center}
.stats div{width:150px;line-height:1.5}
.stats .ic{width:26px;height:26px;border:1px solid var(--line);border-radius:6px;margin:0 auto 10px}
.partners{display:flex;justify-content:center;gap:18px}
.partners div{width:146px;height:48px;border-radius:8px;background:#163049;border:1px solid #23405a}
.feat{display:flex;gap:16px;padding:18px 0;border-bottom:1px solid var(--line)}
.feat .ic{width:34px;height:34px;border-radius:8px;border:1px solid var(--line);flex:none;display:flex;align-items:center;justify-content:center}
.feat h3{font-size:14px;font-weight:600;margin-bottom:6px}
.feat p{font-size:11px;color:var(--muted)}
.testi{display:flex;gap:20px;left:60px;right:60px}
.testi .t{flex:1;background:rgba(13,27,39,.7);border:1px solid var(--line);border-radius:10px;padding:20px;text-align:center;font-size:12px;color:var(--muted);line-height:1.6}
.avatar{width:44px;height:44px;border-radius:50%;background:linear-gradient(135deg,#c9a37a,#6c4e37);margin:0 auto 10px}
.testi .name{color:var(--text);font-size:12px;font-weight:600;margin-bottom:10px}
.posts{display:flex;gap:16px;left:150px;right:150px}
.posts div{flex:1;background:var(--panel-2);border:1px solid var(--line);border-radius:8px;padding:14px 16px;font-size:12px;display:flex;justify-content:space-between;align-items:center}
.field{background:var(--panel-2);border:1px solid var(--line);border-radius:8px;height:40px;padding:0 16px;display:flex;align-items:center;font-size:12px;color:var(--dim)}
.cal{background:var(--panel-2);border:1px solid var(--line);border-radius:10px;padding:22px}
.cal table{width:100%;border-collapse:collapse;font-size:12px;text-align:center}
.cal th{color:var(--muted);font-weight:500;padding:8px 0;font-size:11px}
.cal td{padding:9px 0;color:var(--text)}
.cal td.off{color:var(--dim)}
.cal td.sel span{display:inline-block;width:26px;height:26px;line-height:26px;border-radius:50%;background:var(--accent-2)}
.label{font-size:11px;letter-spacing:.08em;color:var(--muted);font-weight:600;margin-bottom:10px}
.footer-cols{display:flex;gap:80px;font-size:12px;color:var(--muted);line-height:2}
.footer-cols h4{font-size:11px;letter-spacing:.08em;color:var(--text);margin-bottom:6px}
</style>
</head>
<body>
<div class="frame">

  <nav class="abs nav">
    <div class="brand"><span class="mark"></span>Qorvanta</div>
    <ul><li>Services</li><li>Case Studies</li><li>About Us</li><li>Blog</li><li>Contact Us</li></ul>
    <a class="btn">Schedule a Meeting</a>
  </nav>

  <h1 class="abs center hero-title">TURNING COMPLEX CHALLENGES<br><span>INTO SEAMLESS SOLUTIONS</span></h1>
  <p class="abs hero-sub">At Qorvanta, we empower businesses with bespoke software built using advanced AI, platform engineering, system integration, and cloud technologies.</p>
  <div class="abs center" style="top:314px"><a class="btn">Let's Talk</a></div>
  <div class="abs center" style="top:360px"><a class="btn-ghost">Discover More</a></div>
  <div class="abs ghost-word" style="top:390px">QORVANTA</div>

  <!-- Services -->
  <section class="abs card" style="left:112px;width:880px;top:524px;height:620px">
    <div class="abs center eyebrow" style="top:48px">What we do</div>
    <h2 class="abs center section-title" style="top:74px">Driving Innovation Through<br>Tailored Solutions</h2>
    <div class="svc-grid">
      <div class="svc"><div class="ico"><svg width="14" height="14"><circle cx="7" cy="7" r="5" fill="none" stroke="#2fa8ff" stroke-width="1.5"/></svg></div>
        <div class="arrow"><svg width="12" height="12"><path d="M2 10L10 2M4 2h6v6" stroke="#fff" fill="none" stroke-width="1.5"/></svg></div>
        <h3>ARTIFICIAL INTELLIGENCE</h3><p>We build intelligent systems that automate processes, uncover insights and drive smarter decisions across your business.</p></div>
      <div class="svc"><div class="ico"><svg width="14" height="14"><rect x="2" y="2" width="10" height="10" fill="none" stroke="#2fa8ff" stroke-width="1.5"/></svg></div>
        <div class="arrow"><svg width="12" height="12"><path d="M2 10L10 2M4 2h6v6" stroke="#fff" fill="none" stroke-width="1.5"/></svg></div>
        <h3>PLATFORM ENGINEERING</h3><p>We design and develop scalable platforms that integrate with your business systems, enabling flexibility and security for future growth.</p></div>
      <div class="svc"><div class="ico"><svg width="14" height="14"><path d="M2 7h10M7 2v10" stroke="#2fa8ff" stroke-width="1.5"/></svg></div>
        <div class="arrow"><svg width="12" height="12"><path d="M2 10L10 2M4 2h6v6" stroke="#fff" fill="none" stroke-width="1.5"/></svg></div>
        <h3>SYSTEM INTEGRATION</h3><p>Our team connects disparate systems, tools and applications to create seamless workflows, improved efficiency and better data.</p></div>
      <div class="svc"><div class="ico"><svg width="14" height="14"><path d="M3 10h8a3 3 0 0 0-1-6 4 4 0 0 0-7 2 2 2 0 0 0 0 4z" fill="none" stroke="#2fa8ff" stroke-width="1.3"/></svg></div>
        <div class="arrow"><svg width="12" height="12"><path d="M2 10L10 2M4 2h6v6" stroke="#fff" fill="none" stroke-width="1.5"/></svg></div>
        <h3>CLOUD SOLUTIONS</h3><p>We offer modern cloud services that combine flexibility, scalability and security to accelerate your infrastructure and operations.</p></div>
    </div>
    <div class="abs center" style="top:552px"><a class="btn">Let's Discuss Your Project</a></div>
  </section>

  <!-- About -->
  <div class="abs center eyebrow" style="top:1176px">Who we are</div>
  <h2 class="abs center section-title" style="top:1204px">Pioneering Software<br>Engineering Excellence</h2>
  <p class="abs" style="top:1316px;left:232px;width:640px;font-size:12px;color:var(--muted);line-height:1.6;text-align:center">Qorvanta is a team of Australian innovators specialising in custom software development. Whether it's AI-powered tools, scalable platforms, or seamless integrations, we deliver tailored solutions that transform businesses.</p>
  <div class="abs stats" style="top:1406px;left:0;right:0">
    <div><div class="ic"></div>Trusted by top enterprises for mission-critical projects</div>
    <div><div class="ic"></div>10+ years of industry expertise</div>
    <div><div class="ic"></div>A results-driven approach, from concept to deployment</div>
  </div>
  <div class="abs center" style="top:1520px"><a class="btn-ghost">Discover More Us</a></div>
  <div class="abs center" style="top:1576px;font-size:11px;color:var(--muted)">Trusted by top Companies</div>
  <div class="abs partners" style="top:1610px;left:0;right:0"><div></div><div></div><div></div><div></div></div>

  <!-- Why choose -->
  <section class="abs card" style="left:112px;width:880px;top:1764px;height:508px">
    <div class="abs center eyebrow" style="top:44px">Why choose Qorvanta?</div>
    <h2 class="abs center section-title" style="top:68px;font-size:30px">A Partner You Can Trust for Complex Projects</h2>
    <div class="abs" role="img" aria-label="Photo of a team collaborating around laptops in a bright office" style="left:44px;top:132px;width:396px;height:312px;border-radius:10px;background:linear-gradient(135deg,#c7d3d9,#8aa0ad 55%,#5c6f7a)"></div>
    <div class="abs" style="left:470px;top:120px;width:360px">
      <div class="feat"><div class="ic"><svg width="14" height="14"><path d="M2 7l3 3 7-7" stroke="#2fa8ff" fill="none" stroke-width="1.6"/></svg></div><div><h3>CUSTOM SOLUTIONS</h3><p>Every solution is built to match your unique needs.</p></div></div>
      <div class="feat"><div class="ic"><svg width="14" height="14"><circle cx="7" cy="7" r="5" stroke="#2fa8ff" fill="none" stroke-width="1.5"/></svg></div><div><h3>CUTTING-EDGE TECHNOLOGY</h3><p>Leveraging the latest in AI and cloud technologies.</p></div></div>
      <div class="feat"><div class="ic"><svg width="14" height="14"><path d="M2 7h10M8 3l4 4-4 4" stroke="#2fa8ff" fill="none" stroke-width="1.5"/></svg></div><div><h3>END-TO-END COLLABORATION</h3><p>From strategy to implementation, we're with you every step.</p></div></div>
      <div class="feat" style="border:0"><div class="ic"><svg width="14" height="14"><path d="M2 12V8M6 12V5M10 12V2" stroke="#2fa8ff" stroke-width="1.6"/></svg></div><div><h3>PROVEN RESULTS</h3><p>Delivering measurable outcomes that drive growth.</p></div></div>
    </div>
  </section>

  <!-- Testimonials -->
  <div class="abs testi" style="top:2306px">
    <div class="t"><div class="avatar" role="img" aria-label="Client portrait"></div><div class="name">Elena Marsh</div>Qorvanta helped us streamline operations and achieve a 30% boost in efficiency.</div>
    <div class="t"><div class="avatar" role="img" aria-label="Client portrait"></div><div class="name">Elena Marsh</div>Qorvanta helped us streamline operations and achieve a 30% boost in efficiency.</div>
    <div class="t"><div class="avatar" role="img" aria-label="Client portrait"></div><div class="name">Elena Marsh</div>Qorvanta helped us streamline operations and achieve a 30% boost in efficiency.</div>
    <div class="t"><div class="avatar" role="img" aria-label="Client portrait"></div><div class="name">Elena Marsh</div>Qorvanta helped us streamline operations and achieve a 30% boost in efficiency.</div>
  </div>
  <div class="abs center" style="top:2548px"><a class="btn-ghost">See More Success Stories</a></div>

  <!-- Insights -->
  <div class="abs center eyebrow" style="top:2668px">Insights and resources</div>
  <h2 class="abs center section-title" style="top:2696px">Stay Ahead with Expert Insights</h2>
  <p class="abs center" style="top:2746px;font-size:12px;color:var(--muted)">Explore the latest trends, tips, and exclusive strategies from our industry experts</p>
  <div class="abs posts" style="top:2784px">
    <div>The Future of AI in Business <span>›</span></div>
    <div>How Cloud Solutions Drive Growth <span>›</span></div>
    <div>Best Practices for Platform Scalability <span>›</span></div>
  </div>
  <div class="abs center" style="top:2880px"><a class="btn-ghost">Read More Articles</a></div>

  <!-- Contact -->
  <section class="abs card" style="left:112px;width:880px;top:3024px;height:744px">
    <div class="abs center eyebrow" style="top:40px">Let's collaborate</div>
    <h2 class="abs center section-title" style="top:64px;font-size:30px">Ready to Transform Your Business?</h2>
    <p class="abs" style="top:110px;left:190px;width:500px;font-size:12px;color:var(--muted);line-height:1.6;text-align:center">Contact Qorvanta today and let us design the perfect software solution for your needs. Whether you're scaling operations, integrating systems, or embracing AI, we're here to help.</p>
    <div class="abs" style="top:176px;left:44px;right:44px;display:flex;gap:14px">
      <div class="field" style="flex:1">Email</div>
      <div class="field" style="flex:1">Phone</div>
      <a class="btn" style="padding:13px 20px">Get a Free consultation</a>
    </div>
    <div class="abs center" style="top:252px;font-size:16px;font-family:'Space Grotesk',sans-serif;font-weight:500">Book an obligation free consultation with our Lead Technologist</div>
    <div class="abs cal" style="left:44px;top:300px;width:380px;height:400px">
      <div class="avatar" role="img" aria-label="Lead technologist portrait" style="width:40px;height:40px"></div>
      <div style="text-align:center;font-size:12px;color:var(--muted);margin-bottom:12px">Meet with our CTO</div>
      <div class="field" style="height:34px;justify-content:space-between;color:var(--text);margin-bottom:6px"><span>‹</span>January 2026<span>›</span></div>
      <table>
        <tr><th>SUN</th><th>MON</th><th>TUE</th><th>WED</th><th>THU</th><th>FRI</th><th>SAT</th></tr>
        <tr><td class="off">28</td><td class="off">29</td><td class="off">30</td><td class="off">31</td><td>1</td><td>2</td><td>3</td></tr>
        <tr><td>4</td><td>5</td><td>6</td><td>7</td><td>8</td><td>9</td><td>10</td></tr>
        <tr><td>11</td><td>12</td><td>13</td><td>14</td><td>15</td><td>16</td><td>17</td></tr>
        <tr><td>18</td><td>19</td><td class="sel"><span>20</span></td><td>21</td><td>22</td><td>23</td><td>24</td></tr>
        <tr><td>25</td><td>26</td><td>27</td><td>28</td><td>29</td><td>30</td><td>31</td></tr>
      </table>
    </div>
    <div class="abs" style="left:456px;top:300px;width:380px">
      <div class="label">MEETING DURATION</div>
      <div class="field" style="color:var(--text);justify-content:space-between">30 Min<span>⌄</span></div>
      <div class="label" style="margin-top:26px">WHAT TIME WORKS BEST?</div>
      <div style="font-size:11px;color:var(--muted);margin-bottom:10px">Showing Times for <span style="color:var(--accent)">January 20, 2026</span></div>
      <div class="field" style="color:var(--text);justify-content:space-between">10:00 am<span>⌄</span></div>
      <div style="font-size:11px;color:var(--muted);margin-top:14px">UTC +10:00 New South Wales, Canberra</div>
    </div>
  </section>

  <!-- Footer -->
  <footer class="abs" style="left:52px;right:52px;top:3844px">
    <div class="brand" style="position:absolute;left:0;top:0"><span class="mark"></span>Qorvanta</div>
    <div class="footer-cols" style="position:absolute;left:452px;top:0">
      <div><h4>USEFUL LINKS</h4>About Us<br>Case Studies<br>Blog<br>Contact Us</div>
      <div><h4>SERVICES</h4>Artificial Intelligence<br>Platform Engineering<br>System Integration<br>Cloud Solutions</div>
      <div><h4>FOLLOW US</h4><span style="display:flex;gap:10px;margin-top:4px"><svg width="12" height="12"><circle cx="6" cy="6" r="5" fill="#2fa8ff"/></svg><svg width="12" height="12"><circle cx="6" cy="6" r="5" fill="#2fa8ff"/></svg><svg width="12" height="12"><circle cx="6" cy="6" r="5" fill="#2fa8ff"/></svg></span></div>
    </div>
    <div style="position:absolute;left:0;right:0;top:164px;border-top:1px solid var(--line);padding-top:14px;display:flex;justify-content:space-between;font-size:11px;color:var(--muted)">
      <span>© 2025 Qorvanta All Rights Reserved</span><span>Privacy Policy</span>
    </div>
  </footer>
  <div class="abs ghost-word" style="top:3900px">QORVANTA</div>
</div>
</body>
</html>
```